Kestrow Fire Services Pty Ltd

We need business cards for a company based in Perth, we install, service and maintain fire equipment.
On the front we want a great design with our logo and a small spot for our full company name, general company email address and office number. On the back we need space for our name, title, mobile number and email address on the back.

Target Market(s)

Facility managers and commercial/industrial building owners/occupiers.

Contact Information for Business Card

Font styles to use
Sans Serif

Requirements
Must have
• Please only submit 5 of your best samples.
Darker tones are preferred.
Nice to have
• We want to use, black, red and grey. Keep it modern and clean.
I've attached the company logo and a sample of a boarder we use on our emergency plans.
Should not have
• No preference. Let the designer choose.

```html
<!DOCTYPE html>
<html lang="en">
<head>
<meta charset="utf-8">
<title>Kestrow Fire Services – Business Cards</title>
<link rel="stylesheet" href="https://fonts.googleapis.com/css2?family=Hind:wght@300;400;600;700&display=swap">
<style>
  :root {
    --bg-teal: #2e9aa0;
    --bg-sage: #a8cfa8;
    --bg-cream: #fff6b8;
    --fire-red: #ee2630;
    --ink-black: #000000;
    --paper-white: #ffffff;
    --stone-grey: #e5e6e8;
    --text-dark: #111111;
  }
  * { margin: 0; padding: 0; box-sizing: border-box; }
  html, body { width: 1200px; height: 1200px; overflow: hidden; }
  body {
    position: relative;
    font-family: "Hind", sans-serif;
    background: linear-gradient(45deg, var(--bg-teal) 0%, var(--bg-sage) 50%, var(--bg-cream) 100%);
  }
  .card {
    position: absolute;
    overflow: hidden;
    box-shadow: 4px 6px 10px rgba(0, 0, 0, 0.25);
  }
  .card-pattern { position: absolute; inset: 0; }

  /* Front */
  .card-front { left: 246px; top: 147px; width: 712px; height: 407px; background: var(--ink-black); }
  .card-front .card-pattern {
    background: linear-gradient(125deg, #8a1117 0%, #2a0406 35%, #b8161e 60%, #1a0203 80%, #c41a22 100%);
  }
  .company-name {
    position: absolute; left: 59px; top: 35px;
    font-size: 33px; font-weight: 600; color: var(--paper-white); letter-spacing: 0.2px;
    white-space: nowrap;
  }
  .company-contact {
    position: absolute; left: 60px; top: 94px;
    font-size: 25px; font-weight: 300; line-height: 25px; color: var(--paper-white);
  }
  .brand-name {
    position: absolute; right: 41px; top: 326px;
    display: flex; align-items: center; gap: 10px;
    font-size: 40px; font-weight: 600; line-height: 1; color: var(--paper-white);
  }
  .brand-mark {
    width: 18px; height: 18px; background: var(--paper-white); flex: none;
    margin-top: -6px;
  }

  /* Back */
  .card-back { left: 248px; top: 654px; width: 709px; height: 404px; background: var(--paper-white); }
  .card-back .card-pattern {
    background: linear-gradient(125deg, #f4f4f5 0%, var(--stone-grey) 30%, #fafafa 55%, var(--stone-grey) 80%, #f6f6f7 100%);
  }
  .person-name {
    position: absolute; left: 52px; top: 59px;
    font-size: 34.5px; font-weight: 400; color: var(--text-dark); line-height: 1;
  }
  .person-name strong { font-weight: 700; }
  .person-title {
    position: absolute; left: 52px; top: 96px;
    font-size: 24px; font-weight: 400; color: var(--text-dark);
  }
  .contact-rule {
    position: absolute; left: 286px; top: 260px; width: 423px; height: 3px;
    background: var(--fire-red);
  }
  .contact-list { position: absolute; left: 287px; top: 272px; list-style: none; }
  .contact-item {
    display: flex; align-items: center; gap: 10px;
    height: 28.5px;
    font-size: 23.5px; font-weight: 300; color: var(--text-dark);
    white-space: nowrap;
  }
  .contact-icon { width: 23px; height: 23px; flex: none; }
  .contact-text { padding-top: 4px; }
</style>
</head>
<body>

<section class="card card-front">
  <div class="card-pattern" role="img" aria-label="Bold red and black flowing flame-stripe pattern"></div>
  <h1 class="company-name">Kestrow Fire Services Pty Ltd</h1>
  <p class="company-contact">
    123 Street Name, State,<br>
    Country Pincode.<br>
    Ph: +000 12345678<br>
    email@hostname.com
  </p>
  <div class="brand-name"><span class="brand-mark"></span>Kestrow</div>
</section>

<section class="card card-back">
  <div class="card-pattern" role="img" aria-label="Soft light grey and white flowing stripe pattern"></div>
  <h2 class="person-name">FIRST <strong>NAME</strong></h2>
  <p class="person-title">Designation</p>
  <div class="contact-rule"></div>
  <ul class="contact-list">
    <li class="contact-item">
      <svg class="contact-icon" viewBox="0 0 24 24" aria-hidden="true">
        <circle cx="12" cy="12" r="12" fill="#000"/>
        <path d="M12 5.5 L5 11.5 H7 V18 H10.5 V14 H13.5 V18 H17 V11.5 H19 Z" fill="#fff"/>
      </svg>
      <span class="contact-text">123 Street Name, Country Pincode.</span>
    </li>
    <li class="contact-item">
      <svg class="contact-icon" viewBox="0 0 24 24" aria-hidden="true">
        <circle cx="12" cy="12" r="12" fill="#000"/>
        <rect x="8.5" y="5" width="7" height="14" rx="1.5" fill="#fff"/>
        <rect x="9.8" y="7" width="4.4" height="6" fill="#000"/>
      </svg>
      <span class="contact-text">Ph: +000 12345678</span>
    </li>
    <li class="contact-item">
      <svg class="contact-icon" viewBox="0 0 24 24" aria-hidden="true">
        <circle cx="12" cy="12" r="12" fill="#000"/>
        <rect x="5.5" y="7.5" width="13" height="9" fill="#fff"/>
        <path d="M5.5 7.5 L12 13 L18.5 7.5 M5.5 16.5 L10 12 M18.5 16.5 L14 12" stroke="#000" stroke-width="1.1" fill="none"/>
      </svg>
      <span class="contact-text">email@hostname.com</span>
    </li>
  </ul>
</section>

</body>
</html>
```